DL Flyer announcing opening of Willow Fern Cottage Homewares & Gift Store

To create 2 sided full colour DL Flyer which will be distributed by a letterbox drop to announce the opening of a delightful new homewares and gift store called "Willow Fern Cottage Homewares" at 174 Garnet Hill Street, Ashwood.

Willow Fern Cottage Homewares offers a range of exclusive, bespoke, well-crafted decorative homewares and gifts. Our target market is well to do and aspirational, so we want the design of the flyer to match.

The owners, Maureen (a long-time resident of Northbridge) and Lorna have combined their love of homewares and years of retail experience to create this fresh and exciting new store.

Willow Fern Cottage will cater for all those special occasions throughout the year but right now as we move into Christmas we have some beautiful Christmas decorations. Why not come in and visit Lorna who has 18 years experience in the Christmas industry and find out about our Christmas Tree decorating service.

Also we want a call to action so want to offer a 10% discount for people who bring the flyer in during the month of November

The store is open Tuesday to Friday 9.30am to 5.00pm and Saturday 10.00am to 4.00pm

Please find attached duck design we are using the coloured version (excluding the word 'duck' of course). The colour we have chosen for Willow Fern Cottage is "Duck Egg Blue" and the font is Lucida Calligraphy.

Thank you

Target Market(s)

is well to do and aspirational

• Lucida Calligraphy

Colors
cfeae6

Requirements
Must have
• the Duck. Discount voucher, address, look forward to being of service for many years to come. "Duck Egg Blue" colour tones

```html
<!DOCTYPE html>
<html lang="en">
<head>
<meta charset="utf-8">
<title>Willow Fern Cottage Homewares – Opening Flyer</title>
<link rel="stylesheet" href="https://fonts.googleapis.com/css2?family=Berkshire+Swash&family=Open+Sans:ital,wght@0,400;0,600;1,400&display=swap">
<style>
  :root {
    --duck-egg: #8fd6e6;
    --duck-egg-light: #cfeae6;
    --duck-egg-deep: #5cc2da;
    --festive-red: #e8412c;
    --gold: #f8b63a;
    --gold-light: #ffd36a;
    --tree-teal: #3f9fae;
    --ink: #1f2a2e;
    --tag-white: #ffffff;
    --ribbon-orange: #f0642a;
    --ribbon-deep: #c8401a;
  }
  * { margin: 0; padding: 0; box-sizing: border-box; }
  html, body { width: 1200px; height: 2546px; overflow: hidden; }
  body { position: relative; font-family: "Open Sans", sans-serif; }

  .flyer {
    position: absolute; inset: 0; overflow: hidden;
    background: radial-gradient(ellipse at 30% 20%, var(--duck-egg-light) 0%, var(--duck-egg) 55%, var(--duck-egg-deep) 100%);
  }
  .bokeh-backdrop {
    position: absolute; inset: 0;
    background:
      radial-gradient(circle at 18% 38%, rgba(255,255,255,.28) 0 180px, transparent 181px),
      radial-gradient(circle at 88% 8%, rgba(255,255,255,.22) 0 140px, transparent 141px),
      radial-gradient(circle at 8% 82%, rgba(255,255,255,.2) 0 160px, transparent 161px),
      radial-gradient(circle at 92% 62%, rgba(255,255,255,.18) 0 120px, transparent 121px);
  }

  /* Brand block */
  .brand-mark {
    position: absolute; left: 200px; top: 150px; width: 280px; height: 280px;
    border-radius: 50%; background: rgba(255,255,255,.55);
  }
  .brand-name {
    position: absolute; left: 520px; top: 120px; width: 520px;
    font-family: "Berkshire Swash", cursive; font-size: 92px; line-height: 1.15;
    color: var(--festive-red); text-align: center;
  }

  .stars { position: absolute; }
  .rule { position: absolute; height: 3px; background: var(--festive-red); }

  .intro-title {
    position: absolute; left: 0; top: 770px; width: 1200px; text-align: center;
    font-family: "Berkshire Swash", cursive; font-size: 56px; color: var(--gold-light);
    text-shadow: 0 0 3px var(--ribbon-orange), 2px 2px 0 var(--ribbon-orange);
  }
  .intro-copy {
    position: absolute; left: 150px; top: 860px; width: 900px; text-align: center;
    font-style: italic; font-size: 44px; line-height: 76px; letter-spacing: 1px;
    color: var(--festive-red);
  }
  .intro-copy p + p { margin-top: 16px; }

  .tree-illustration {
    position: absolute; left: 180px; top: 1520px; width: 840px; height: 990px;
    background: radial-gradient(ellipse at 50% 55%, rgba(63,159,174,.55) 0%, rgba(63,159,174,.25) 55%, transparent 75%);
  }

  .tag {
    position: absolute; background: var(--tag-white); border-radius: 22px;
    box-shadow: 4px 6px 12px rgba(0,0,0,.25);
    outline: 4px dashed var(--festive-red); outline-offset: -16px;
    color: var(--ink); text-align: center;
  }
  .tag--hours {
    left: -10px; top: 1620px; width: 640px; height: 300px;
    transform: rotate(20deg); padding: 48px 30px;
    font-size: 42px; line-height: 58px;
  }
  .tag--voucher {
    left: 380px; top: 2200px; width: 620px; height: 260px;
    transform: rotate(-20deg); padding: 40px 36px;
    font-size: 40px; line-height: 58px; text-align: left;
  }

  .address {
    position: absolute; left: 10px; top: 2140px; width: 760px;
    transform: rotate(-25deg); text-align: center;
    font-size: 46px; font-weight: 600; color: var(--tag-white);
    text-shadow: -2px -2px 0 var(--tree-teal), 2px -2px 0 var(--tree-teal), -2px 2px 0 var(--tree-teal), 2px 2px 0 var(--tree-teal);
  }

  .discount-ribbon {
    position: absolute; left: 820px; top: 1820px; width: 300px; height: 240px;
    transform: rotate(-20deg);
    background: linear-gradient(180deg, var(--ribbon-orange), var(--ribbon-deep));
    border-radius: 14px;
    color: var(--tag-white); font-weight: 600; font-size: 140px; line-height: 240px;
    text-align: center; letter-spacing: -4px;
  }
  .discount-ribbon sup { font-size: 70px; vertical-align: 60px; }
</style>
</head>
<body>
<main class="flyer">
  <div class="bokeh-backdrop" role="img" aria-label="Soft blurred Christmas baubles and snowflakes on duck egg blue"></div>

  <header>
    <div class="brand-mark" aria-hidden="true"></div>
    <h1 class="brand-name">Willow Fern Cottage Homewares</h1>
  </header>

  <svg class="stars" style="left:370px;top:610px" width="460" height="70" viewBox="0 0 460 70" aria-hidden="true">
    <g fill="#e8412c">
      <polygon points="35,2 44,26 69,26 49,42 57,68 35,52 13,68 21,42 1,26 26,26"/>
      <polygon points="230,2 239,26 264,26 244,42 252,68 230,52 208,68 216,42 196,26 221,26"/>
      <polygon points="425,2 434,26 459,26 439,42 447,68 425,52 403,68 411,42 391,26 416,26"/>
    </g>
  </svg>
  <div class="rule" style="left:72px;top:712px;width:1056px"></div>
  <div class="rule" style="left:130px;top:728px;width:940px;height:2px"></div>

  <section>
    <h2 class="intro-title">Willow Fern Cottage Homewares</h2>
    <div class="intro-copy">
      <p>offers a range of exclusive, bespoke, well-crafted decorative homewares and gifts</p>
      <p>18 years experience in the Christmas industry and find out about our Christmas Tree decorating service.</p>
    </div>
  </section>

  <div class="rule" style="left:72px;top:1458px;width:1056px"></div>
  <div class="rule" style="left:130px;top:1474px;width:940px;height:2px"></div>
  <svg class="stars" style="left:370px;top:1505px" width="460" height="70" viewBox="0 0 460 70" aria-hidden="true">
    <g fill="#e8412c">
      <polygon points="35,2 44,26 69,26 49,42 57,68 35,52 13,68 21,42 1,26 26,26"/>
      <polygon points="230,2 239,26 264,26 244,42 252,68 230,52 208,68 216,42 196,26 221,26"/>
      <polygon points="425,2 434,26 459,26 439,42 447,68 425,52 403,68 411,42 391,26 416,26"/>
    </g>
  </svg>

  <div class="tree-illustration" role="img" aria-label="Swirling teal Christmas tree with star topper"></div>

  <div class="tag tag--hours">Tuesday to Friday 9.30am to 5.00pm and Saturday 10.00am to 4.00pm</div>

  <p class="address">174 Garnet Hill Street, Ashwood</p>

  <div class="discount-ribbon">-10<sup>%</sup></div>
  <div class="tag tag--voucher">discount for people who bring the flyer in during the month of November</div>
</main>
</body>
</html>
```